Debt Collection Website Design! We are the solution for landlords to get paid what they are owed.

We are a 3rd party debt collection company that specializes in Residential and Commercial real estate debt collection. We help landlords recover money from past residents by being fair, friendly and aggressive. We also collect/buy/sell/trade civil judgments won resulting from anything from automobile accidents to evictions to a pet zebra getting stolen. We buy single judgments to large portfolios, we also collect judgments for a nominal fee.

I would like a new, modern, easy to navigate website. A spot that we can post news stories or updated information about our company. I have included our company logo that must be on the top of the page. Feel free to ask any questions that will help get the process going.

Target Market(s)

Landlords, small to large apartment complex. Real estate services and lawyers.

Industry/Entity Type

Real Estate

Number of Pages Required

3 page

Requirements
Must have
• Company logo which has been attached. A page where we can explain the collection process, fees and placement. A page where we can explain judgments, collection vs. selling, placement form. I am open to any font/designs and willing to work with anyone.
Nice to have
• Nice to have a spot on the homepage to place news articles about ourselves and our industry.
Should not have
• I don't want it over crowded. Simple, sleek and easy to navigate is best. No gavels on any of the pages. It cannot look legal, say/show anything that we use legal powers to collect. We are not a law office, we don't practice law, we are 3rd party debt collection agency.

```html
<!DOCTYPE html>
<html lang="en">
<head>
<meta charset="utf-8">
<title>Halvard Recovery, LLC</title>
<link href="https://fonts.googleapis.com/css2?family=Roboto:ital,wght@0,300;0,400;0,500;1,300;1,400&family=Varela+Round&display=swap" rel="stylesheet">
<style>
  :root {
    --navy: #1c2f7a;
    --navy-deep: #142668;
    --heading: #1e3374;
    --text: #4a4a4a;
    --muted: #7b8490;
    --panel: #7e8794;
    --panel-rule: #9aa2ad;
    --rule: #d5d5d5;
    --white: #ffffff;
    --icon-grey: #a7a7a7;
  }
  * { box-sizing: border-box; margin: 0; padding: 0; }
  html, body { width: 954px; height: 1200px; overflow: hidden; background: var(--white); }
  body { position: relative; font-family: "Roboto", sans-serif; color: var(--text); }
  .abs { position: absolute; }

  /* Header */
  .brand { left: 59px; top: 22px; display: flex; align-items: center; gap: 8px; }
  .brand-mark { width: 30px; height: 30px; background: var(--navy); }
  .brand-name { font-size: 19px; font-weight: 400; color: var(--navy); line-height: 1.05; letter-spacing: .3px; }
  .brand-name small { display: block; font-size: 10px; letter-spacing: 1px; }
  .call { right: 59px; top: 32px; font-size: 14px; color: var(--heading); display: flex; align-items: center; gap: 8px; }
  .call b { font-weight: 400; color: #222; }

  /* Navigation */
  .nav { left: 59px; top: 73px; width: 836px; height: 36px; background: linear-gradient(var(--navy), var(--navy-deep)); display: flex; align-items: center; padding-left: 16px; }
  .nav a { color: var(--white); text-decoration: none; font-size: 9.5px; letter-spacing: .4px; margin-right: 44px; }

  /* Hero */
  .hero { left: 59px; top: 111px; width: 836px; height: 282px; background: linear-gradient(90deg, #5a5a5a 0%, #6d6a66 45%, #8a7f70 100%); overflow: hidden; }
  .hero-photo { position: absolute; right: 0; top: 0; width: 420px; height: 282px; background: radial-gradient(circle at 55% 60%, #c9b27a 0%, #a08a66 18%, #3a3a3e 55%, #555 100%); }
  .hero-title { position: absolute; left: 24px; top: 40px; width: 430px; font-family: "Varela Round", sans-serif; font-size: 24.5px; line-height: 31.5px; color: var(--white); }
  .hero-btn { position: absolute; left: 24px; top: 186px; width: 126px; height: 32px; background: var(--white); color: var(--heading); font-family: "Varela Round", sans-serif; font-size: 17px; display: flex; align-items: center; justify-content: center; }
  .dots { position: absolute; left: 24px; top: 253px; display: flex; gap: 5px; }
  .dots i { width: 9px; height: 9px; border-radius: 50%; background: var(--white); }
  .dots i.off { background: #a9a9a9; }

  /* Main */
  h2 { font-weight: 400; color: var(--heading); font-size: 18px; }
  .copy { font-size: 9.5px; line-height: 18.3px; color: var(--text); }
  .rule { height: 1px; background: var(--rule); }
  .link { font-size: 9.5px; font-weight: 500; color: var(--heading); letter-spacing: .3px; }

  .welcome { left: 59px; top: 419px; width: 552px; }
  .welcome h2 { margin-bottom: 10px; }
  .services { left: 59px; top: 561px; width: 552px; }
  .services h2 { margin-bottom: 5px; }
  .service { width: 263px; top: 650px; }
  .service .pic { height: 123px; }
  .service h3 { font-weight: 400; font-size: 14px; color: var(--heading); margin: 12px 0 4px; }
  .service .copy { font-size: 9.3px; line-height: 17px; }
  .service .link { display: block; margin-top: 6px; }
  .pic-homes { background: linear-gradient(180deg, #5d8fc8 0%, #9ab7d6 45%, #8c7a66 70%, #b7a58d 100%); }
  .pic-office { background: linear-gradient(135deg, #a9bfd6 0%, #3b5a8a 50%, #d5dde6 100%); }

  /* Sidebar */
  .panel { background: var(--panel); color: var(--white); padding: 14px 16px; }
  .panel h2 { color: var(--white); font-size: 17.5px; font-weight: 300; }
  .news { left: 631px; top: 423px; width: 258px; height: 265px; }
  .news-item { border-bottom: 1px solid var(--panel-rule); padding: 8px 0 8px; }
  .news-item:last-of-type { border-bottom: 0; }
  .news-date { font-size: 10px; color: var(--navy); }
  .news-text { font-size: 8.6px; font-style: italic; font-weight: 300; line-height: 14.5px; color: #eef0f3; margin-top: 3px; }
  .panel-btn { display: inline-block; background: var(--navy); color: var(--white); font-size: 9px; letter-spacing: .4px; padding: 8px 16px; margin-top: 4px; }
  .testi { left: 631px; top: 701px; width: 264px; height: 191px; }
  .testi-text { font-size: 8.6px; font-style: italic; font-weight: 300; line-height: 16.8px; color: #eef0f3; margin-top: 10px; }
  .person { display: flex; align-items: center; gap: 12px; margin-top: 8px; }
  .avatar { width: 43px; height: 43px; background: linear-gradient(#dfe3ea, #3b4660); }
  .person b { display: block; font-weight: 400; font-size: 9.5px; }
  .person i { font-size: 8.6px; font-weight: 300; }

  /* Team & blog */
  .team { left: 59px; top: 947px; width: 555px; }
  .arrows { position: absolute; top: 4px; display: flex; gap: 12px; }
  .team-photo { left: 59px; top: 983px; width: 97px; height: 102px; border: 2px solid #ddd; background: linear-gradient(#e5e9ee, #2d3650); }
  .team-body { left: 172px; top: 980px; width: 440px; }
  .team-body h3, .blog-body h3 { font-weight: 400; font-size: 13px; color: var(--heading); margin-bottom: 3px; }
  .team-body .copy, .blog-body .copy { font-size: 9.3px; line-height: 17px; }
  .connect { display: flex; align-items: center; gap: 4px; margin-top: 10px; font-size: 9.5px; color: var(--muted); }
  .connect span { margin-right: 8px; }
  .connect i { width: 23px; height: 23px; border-radius: 50%; background: var(--icon-grey); }
  .vline { left: 620px; top: 952px; width: 1px; height: 134px; background: var(--rule); }
  .blog { left: 641px; top: 947px; width: 254px; }
  .blog-body { left: 641px; top: 980px; width: 254px; }
  .posted { font-size: 9px; font-style: italic; color: var(--heading); margin-top: 8px; }

  /* Footer */
  .footer { left: 0; top: 1115px; width: 954px; height: 85px; background: var(--navy); }
  .foot-mark { position: absolute; left: 59px; top: 31px; width: 26px; height: 26px; background: var(--white); }
  .foot-copy { position: absolute; left: 103px; top: 31px; font-size: 8.6px; line-height: 14px; color: #a9b4d8; font-weight: 300; }
  .foot-social { position: absolute; right: 59px; top: 30px; display: flex; align-items: center; gap: 4px; font-size: 8.5px; color: var(--white); letter-spacing: .3px; }
  .foot-social span { margin-right: 8px; }
  .foot-social i { width: 23px; height: 23px; border-radius: 50%; background: var(--white); }
</style>
</head>
<body>

<header>
  <div class="abs brand"><span class="brand-mark"></span><span class="brand-name">Halvard<small>RECOVERY, LLC</small></span></div>
  <div class="abs call">
    <svg width="12" height="12" viewBox="0 0 12 12"><rect width="12" height="12" rx="2" fill="#222"/><path d="M3.5 2.5l1.6 1.8-.8 1.1c.6 1.1 1.3 1.8 2.3 2.3l1.1-.8 1.8 1.6-.9 1.1C5.8 9.4 2.7 6.3 2.4 3.4z" fill="#fff"/></svg>
    Call Us: <b>555-018-4270</b>
  </div>
  <nav class="abs nav">
    <a>HOME</a><a>ABOUT US</a><a>SERVICES</a><a>LATEST NEWS</a><a>BLOG</a><a>TESTIMONIALS</a><a>CAREER</a><a>OUR TEAM</a><a>CONTACT US</a>
  </nav>
</header>

<section class="abs hero">
  <div class="hero-photo" role="img" aria-label="Businessman holding a gold piggy bank surrounded by floating dollar signs"></div>
  <h1 class="hero-title" style="font-weight:400">We are a Debt Collection Company that Specializes in Residential and Commercial Real Estate Debt Collection..</h1>
  <div class="hero-btn">Read More</div>
  <div class="dots"><i class="off"></i><i></i><i></i><i></i></div>
</section>

<section class="abs welcome">
  <h2>Welcome to Our Website</h2>
  <p class="copy">Aliquam molestie, mi et imperdiet euismod, dui purus auctor tellus, et interdum lacus lectus et ante. Sed accumsan sollicitudin sapien, sit amet adipiscing turpis gravida ac. In congue, neque ac lobortis volutpat, libero mauris varius mi, vitae suscipit ipsum ligula vitae risus. Duis aliquam nibh a dui iaculis viverra id a velit. Vivamus egestas risus in magna varius commodo. Sed semper viverra egestas. Etiam pretium porttitor lectus, vel ornare neque porta volutpat.</p>
</section>
<div class="abs rule" style="left:59px;top:547px;width:552px"></div>

<section class="abs services">
  <h2>Our Services</h2>
  <p class="copy">Aliquam molestie, mi et imperdiet euismod, dui purus auctor tellus, et interdum lacus lectus et ante. Sed accumsan sollicitudin sapien, sit amet adipiscing turpis gravida ac. In congue, neque ac lobortis volutpat, libero mauris varius mi, vitae suscipit ipsum ligula vitae risus.</p>
</section>

<article class="abs service" style="left:59px">
  <div class="pic pic-homes" role="img" aria-label="Row of residential townhouses under a blue sky"></div>
  <h3>Residential</h3>
  <p class="copy">Aliquam molestie, mi et imperdiet euismod, dui purus auctor tellus, et interdum lacus lectus et ante. Sed accumsan sollicitudin sapien, sit amet adipiscing turpis gravida ac. In congue, neque ac lobortis volutpat...</p>
  <span class="link">READ MORE</span>
</article>
<article class="abs service" style="left:346px">
  <div class="pic pic-office" role="img" aria-label="Business people signing documents at an office desk"></div>
  <h3>Commercial</h3>
  <p class="copy">Aliquam molestie, mi et imperdiet euismod, dui purus auctor tellus, et interdum lacus lectus et ante. Sed accumsan sollicitudin sapien, sit amet adipiscing turpis gravida ac. In congue, neque ac lobortis volutpat...</p>
  <span class="link">READ MORE</span>
</article>

<aside class="abs panel news">
  <h2>Latest News</h2>
  <div class="news-item"><div class="news-date">Feb 23, 2015</div><p class="news-text">Aliquam molestie, mi et imperdiet euismod, dui purus auctor tellus, et interdum lacus lectus....</p></div>
  <div class="news-item"><div class="news-date">Feb 23, 2015</div><p class="news-text">Aliquam molestie, mi et imperdiet euismod, dui purus auctor tellus, et interdum lacus lectus....</p></div>
  <div class="news-item"><div class="news-date">Feb 23, 2015</div><p class="news-text">Aliquam molestie, mi et imperdiet euismod, dui purus auctor tellus, et interdum lacus lectus....</p></div>
  <span class="panel-btn">READ MORE</span>
</aside>

<aside class="abs panel testi">
  <h2>Testimonials</h2>
  <p class="testi-text"><svg width="16" height="10" viewBox="0 0 16 10" style="margin-right:6px"><path d="M0 10V5L3 0h3L4 5h3v5zM9 10V5l3-5h3l-2 5h3v5z" fill="#fff"/></svg>Aliquam molestie, mi et imperdiet euismod, dui purus auctor tellus, et interdum lacus lectus et ante. Sed accumsan sollicitudin sapien, sit amet adipiscing turpis gravida ac. In congue, neque ac lobortis volutpat...</p>
  <div class="person"><div class="avatar" role="img" aria-label="Portrait of the client"></div><div><b>Name goes here</b><i>City Name</i></div></div>
</aside>

<div class="abs rule" style="left:59px;top:928px;width:836px"></div>

<section class="abs team">
  <h2>Our Team</h2>
  <div class="arrows" style="right:0">
    <svg width="10" height="14" viewBox="0 0 10 14"><path d="M8 1L2 7l6 6" fill="none" stroke="#333" stroke-width="1.5"/></svg>
    <svg width="10" height="14" viewBox="0 0 10 14"><path d="M2 1l6 6-6 6" fill="none" stroke="#333" stroke-width="1.5"/></svg>
  </div>
</section>
<div class="abs team-photo" role="img" aria-label="Portrait of a team member in a suit"></div>
<div class="abs team-body">
  <h3>Name goes here</h3>
  <p class="copy">Aliquam molestie, mi et imperdiet euismod, dui purus auctor tellus, et interdum lacus lectus et ante. Sed accumsan sollicitudin sapien, sit amet adipiscing turpis gravida ac. In congue, neque ac lobortis volutpat...</p>
  <div class="connect"><span>Connect:</span><i></i><i></i><i></i><i></i></div>
</div>

<div class="abs vline"></div>

<section class="abs blog">
  <h2>Blog</h2>
  <div class="arrows" style="right:0">
    <svg width="10" height="14" viewBox="0 0 10 14"><path d="M8 1L2 7l6 6" fill="none" stroke="#333" stroke-width="1.5"/></svg>
    <svg width="10" height="14" viewBox="0 0 10 14"><path d="M2 1l6 6-6 6" fill="none" stroke="#333" stroke-width="1.5"/></svg>
  </div>
</section>
<div class="abs blog-body">
  <h3>Vestibulum ante ipsum primis</h3>
  <p class="copy">Aliquam molestie, mi et imperdiet euismod, dui purus auctor tellus, et interdum lacus lectus et ante. Sed accumsan sollicitudin sapien, sit amet adipiscing turpis gravida ac. In congue, neque ac lobortis volutpat...</p>
  <p class="posted">Posted on 2 hrs ago</p>
</div>

<footer class="abs footer">
  <span class="foot-mark"></span>
  <p class="foot-copy">Copyright © 2015.Company Name.All Right Reserved<br>Privacy Policy &nbsp;|&nbsp; Term of Services</p>
  <div class="foot-social"><span>CONNECT US</span><i></i><i></i><i></i><i></i></div>
</footer>

</body>
</html>
```